Oberwynn: need two labels and packaging for coffee scrub circular jar with lid *

What I need

A small sticker for the front of the round jar
A sticker for the bottom of the jar
A sticker can go at the top of the sticker depending on the design (open to suggestions)
I will need two different packaging designs for the two flavours (golden quiver and original vanilla). Both flavours should have same theme with changes made to ingredients. For obvious reasons, the flavour should be displayed on the front of the jar in product info.
‘Useful information’ for both products are stated down below. Depending on what looks best I do not mind if not all information is mentioned. The description and benefits of the product can be modified once added to packaging. No modifications should be made to the ‘ingredients’ and ‘how to use’ text.

I am flexible about the design of the packaging and open to suggestions. I am not too keen on the logo and believe the logo takes up too much attention to emphasise the product attributes. I also don’t like the white background of the sticker and the lengthy information plotted on the sides of the jar. I want design to be simplistic ...to reflect the simple ingredients. However, it must also look professional to justify paying £15.99 for product.

About Oberwynn

This is a coffee scrub all organic and VEGAN / VEGAN friendly product. The packaging should look professional and promote the natural ingredients of the product. Attached is the existing design. I will change the existing container to a circular round jar that has a metallic or black metallic lid. Lid will also cover the rim of the product.
Ingredients
Oberwynn currently has two different flavours.
Original Coffee Scrub
Golden Quiver Coffee Scrub
Original Coffee Scrub Ingredients: Coffea Robusta Seed Powder, Sucrose, Sodium Chloride, Cocos Nucifera Oil, Prunus Amygdalus Dulcis Oil, Tocopherol, Vanilla Planitfolia Fruit Oil.
Golden Quiver Coffee Scrub Ingredients: Coffee Robusta Seed Powder, Sucrose, Sodium Chloride, Cocos Nucifera Oil, Citrus Aurantium Dulcis Oil, Citrus Aurantium Dulcis Peel Powder, Citrus Limon Peel Oil, Tocopherol, Vanilla Planitfolia Fruit Oil.

Useful information for the ORIGINAL FLAVOUR packaging

Modifications can be made to ‘Description’ and ‘Benefits’ if need be. NO modification should be made to ‘How to use’ & ‘Ingredients’.

Description: A powerful coffee scrub, blended with himilayan pink salt, demerara sugar and purifying natural oils. Suitable for normal to dry skin.
Benefits:
A stimulating body scrub with a carefully selected blend of ingredients
Invigorating, exfoliating, nourishing
Natural anti-ageing

How to use: Apply scrub to body in bath or shower in circular motions while skin is damp. Leave for 5-10 minutes before washing off with warm water. Suitable for face and body.

Ingredients used:
Made in the U.K

Useful information for the Golden Quiver packaging

Description: Feel fresh, smell fresh, with the citrus scented coffee scrub. Suitable for normal to dry skin.
Benefits:
Contains real orange and lemon peels to brighten your skin
Natural anti-ageing

Ingredients used:
Made in the U.K

Advisory Information
Suitable for vegetarians and vegans. Not for internal use. Avoid contact with eyes. Do not apply to broken or irritated skin. If sensitivity occurs discontinue use. Avoid this product if you are allergic or sensitive to any of the ingredients. Keep out of reach of children. Do not use on animals. Store in a cool, dry place out of direct sunlight.

Attached images
The attached images show the original and current packaging. Feel free to use in order to understand more about product.

Target Market(s)

18-35 year old females into natural skincare and organic. Possibly have dry skin or skin condition such as psoriasis, acne, discoloration etc.

Industry/Entity Type

Skin Care Product

Colors

Designer to choose colors to be used in the design.

Requirements
Must have
• Must be simple yet sophisticated design. Must include the 'How to use' and 'Ingredients' specifically to the different flavors.
• Must have design that can be suitable against transparent and colored background.
Nice to have
• Not happy with the logo it should be changed to something smaller and simpler design. Designer must ensure the logo is suitable against colored and transparent backgrounds.
• Designer can decide if she/he wants a sticker on the top of the lid or at the bottom, at the side or all 3. Once I am happy with the packaging I can change the container to suit this.
Should not have
• Make sure to not have too much color it needs to be simple and yet represent a feminine and professional looking brand. Remember, the 'Description' and 'Benefits' can be condensed. More importantly, not too much clutter or text on packaging.

```html
<!DOCTYPE html>
<html lang="en">
<head>
<meta charset="utf-8">
<title>Oberwynn Coffee Scrub Labels</title>
<link href="https://fonts.googleapis.com/css2?family=Montserrat:wght@800&family=Nunito:wght@400;700&family=Quicksand:wght@500;600&display=swap" rel="stylesheet">
<style>
  :root{
    --cream:#fefad3;
    --ring:#bfe3a8;
    --panel:#efe2b9;
    --brown:#7a5712;
    --orange:#f39a27;
    --ink:#1a1a1a;
    --edge:#9a9a9a;
    --leaf:#5aa83a;
  }
  *{margin:0;padding:0;box-sizing:border-box}
  html,body{width:1200px;height:667px;overflow:hidden;background:#fff}
  .sheet{position:relative;width:1200px;height:667px;font-family:"Nunito",sans-serif;color:var(--ink)}

  .lid{position:absolute;width:246px;height:246px;border-radius:50%;background:var(--cream);
       display:flex;flex-direction:column;align-items:center}
  .lid::after{content:"";position:absolute;inset:9px;border:4px solid var(--ring);border-radius:50%}
  .lid--vanilla{left:54px;top:14px}
  .lid--golden{left:327px;top:15px}
  .brand{font-family:"Montserrat",sans-serif;font-weight:800;letter-spacing:.2em;color:var(--ink);line-height:1}
  .tagline{font-family:"Quicksand",sans-serif;font-weight:500;letter-spacing:.12em;color:#555;line-height:1}
  .lid .brand{font-size:19px;margin-top:52px;margin-left:.2em}
  .lid .tagline{font-size:6px;margin-top:4px}
  .lid .flavour{font-family:"Quicksand",sans-serif;font-weight:600;font-size:21px;letter-spacing:.04em;
       text-align:center;line-height:30px;margin-top:38px;color:var(--brown)}
  .flavour .accent{color:var(--orange)}

  .wrap{position:absolute;left:17px;width:1167px;height:200px;background:var(--cream);border:1px solid var(--edge)}
  .wrap--golden{top:258px}
  .wrap--vanilla{top:467px}
  .panel{position:absolute;top:15px;height:170px;background:var(--panel);border-radius:4px;
       font-size:9.2px;line-height:11.7px;padding:11px 4px 11px 8px}
  .panel--info{left:31px;width:337px}
  .panel--care{left:625px;width:272px;padding-left:14px}
  .panel b{font-weight:700}
  .panel p+p{margin-top:11.7px}

  .front{position:absolute;left:370px;width:250px;top:22px;text-align:center}
  .front .brand{font-size:21px;margin-left:.2em}
  .front .tagline{font-size:7px;margin-top:5px}
  .front .flavour{font-family:"Quicksand",sans-serif;font-weight:500;font-size:21px;letter-spacing:.08em;
       line-height:25px;margin-top:22px;color:var(--brown)}
  .front .skin{font-size:11px;margin-top:30px;color:var(--brown)}

  .specs{position:absolute;left:936px;top:16px;width:200px;height:170px}
  .site{font-size:11.5px;letter-spacing:.02em}
  .vegan-badge{position:absolute;left:0;top:50px;width:64px;height:36px;background:var(--leaf);border-radius:18px}
  .pao{position:absolute;left:0;top:105px}
  .weight{position:absolute;left:0;top:150px;font-size:18px}
  .code-slot{position:absolute;left:84px;top:43px;width:76px;height:127px;border:1px solid var(--ink);
       display:flex;align-items:center;justify-content:center}
  .code-slot span{writing-mode:vertical-rl;font-weight:700;font-size:17px}
</style>
</head>
<body>
<div class="sheet">

  <div class="lid lid--vanilla">
    <div class="brand">OBERWYNN</div>
    <div class="tagline">PURE RITUAL</div>
    <div class="flavour">ORIGINAL VANILLA<br>COFFEE SCRUB</div>
  </div>

  <div class="lid lid--golden">
    <div class="brand">OBERWYNN</div>
    <div class="tagline">PURE RITUAL</div>
    <div class="flavour"><span class="accent">GOLDEN QUIVER</span><br>COFFEE SCRUB</div>
  </div>

  <section class="wrap wrap--golden">
    <div class="panel panel--info">
      <p><b>Ingredients</b>: Coffee Robusta Seed Powder, Sucrose, Sodium Chloride,<br>Cocos Nucifera Oil, Citrus Aurantium Dulcis Oil, Citrus Aurantium Dulcis<br>Peel Powder, Citrus Limon Peel Oil, Tocopherol, Vanilla Planitfolia Fruit Oil.</p>
      <p><b>Made in the U.K</b></p>
      <p><b>Advisory Information</b><br>Suitable for vegetarians and vegans. Not for internal use. Avoid contact<br>with eyes. Do not apply to broken or irritated skin. If sensitivity occurs<br>discontinue use. Avoid this product if you are allergic or sensitive to any<br>of the ingredients. Keep out of reach of children. Do not use on animals.<br>Store in a cool, dry place out of direct sunlight.</p>
    </div>
    <div class="front">
      <div class="brand">OBERWYNN</div>
      <div class="tagline">PURE RITUAL</div>
      <div class="flavour"><span class="accent">GOLDEN QUIVER</span><br>COFFEE SCRUB</div>
      <div class="skin">Suitable for normal to dry skin.</div>
    </div>
    <div class="panel panel--care">
      <p><b>Benefits:</b><br>Contains real orange and lemon peels to brighten your<br>skin. Invigorating, exfoliating, nourishing and<br>natural anti-ageing.</p>
      <p><b>How to use</b>: Apply scrub to body in bath or shower in<br>circular motions while skin is damp.<br>Leave for 5-10 minutes before washing off with warm<br>water. Suitable for face and body.</p>
    </div>
    <div class="specs">
      <div class="site">WWW.OBERWYNN.COM</div>
      <div class="vegan-badge" role="img" aria-label="Vegan certification badge"></div>
      <svg class="pao" width="40" height="38" viewBox="0 0 40 38" role="img" aria-label="12 months after opening">
        <path d="M2 12 L34 2" stroke="#1a1a1a" stroke-width="2" fill="none"/>
        <path d="M3 15 L35 5" stroke="#1a1a1a" stroke-width="1.2" fill="none"/>
        <rect x="3" y="18" width="33" height="18" rx="3" fill="none" stroke="#1a1a1a" stroke-width="1.5"/>
        <text x="19.5" y="32" font-size="10" text-anchor="middle" font-family="Nunito,sans-serif">12M</text>
      </svg>
      <div class="weight">200g</div>
      <div class="code-slot"><span>barcode here</span></div>
    </div>
  </section>

  <section class="wrap wrap--vanilla">
    <div class="panel panel--info">
      <p><b>Ingredients</b>: Coffea Robusta Seed Powder, Sucrose, Sodium Chloride,<br>Cocos Nucifera Oil, Prunus Amygdalus Dulcis Oil, Tocopherol,<br>Vanilla Planitfolia Fruit Oil.</p>
      <p><b>Made in the U.K</b></p>
      <p><b>Advisory Information</b><br>Suitable for vegetarians and vegans. Not for internal use. Avoid contact<br>with eyes. Do not apply to broken or irritated skin. If sensitivity occurs<br>discontinue use. Avoid this product if you are allergic or sensitive to any<br>of the ingredients. Keep out of reach of children. Do not use on animals.<br>Store in a cool, dry place out of direct sunlight.</p>
    </div>
    <div class="front">
      <div class="brand">OBERWYNN</div>
      <div class="tagline">PURE RITUAL</div>
      <div class="flavour">ORIGINAL VANILLA<br>COFFEE SCRUB</div>
      <div class="skin">Suitable for normal to dry skin.</div>
    </div>
    <div class="panel panel--care">
      <p><b>Benefits:</b><br>A stimulating body scrub with a carefully selected blend<br>of ingredients. Invigorating, exfoliating, nourishing and<br>natural anti-ageing.</p>
      <p><b>How to use</b>: Apply scrub to body in bath or shower in<br>circular motions while skin is damp.<br>Leave for 5-10 minutes before washing off with warm<br>water. Suitable for face and body.</p>
    </div>
    <div class="specs">
      <div class="site">WWW.OBERWYNN.COM</div>
      <div class="vegan-badge" role="img" aria-label="Vegan certification badge"></div>
      <svg class="pao" width="40" height="38" viewBox="0 0 40 38" role="img" aria-label="12 months after opening">
        <path d="M2 12 L34 2" stroke="#1a1a1a" stroke-width="2" fill="none"/>
        <path d="M3 15 L35 5" stroke="#1a1a1a" stroke-width="1.2" fill="none"/>
        <rect x="3" y="18" width="33" height="18" rx="3" fill="none" stroke="#1a1a1a" stroke-width="1.5"/>
        <text x="19.5" y="32" font-size="10" text-anchor="middle" font-family="Nunito,sans-serif">12M</text>
      </svg>
      <div class="weight">200g</div>
      <div class="code-slot"><span>barcode here</span></div>
    </div>
  </section>

</div>
</body>
</html>
```